Branded Event Kit: Step & Repeat Banner, Canopy Tent, and Table Cover Design

Who We Are:
https://www.getmarlo.com/

Project Overview:
I am looking for a cohesive, eye-catching design across three branded event materials that align with our branding:

What's Needed:
- 8x8 Step and Repeat Fabric Banner
- 10x10 Custom Canopy Tent (with sides and back)
- Stretch Table Cover with Zipper Back

Design Goals:
- Visually striking, clean, and modern design
- Seamless brand integration across all three pieces
- Easy readability and strong brand recognition from a distance
- Consistent layout, typography, and color use across all materials

Deliverables:
- Print-ready designs for each template (tent, banner, table cover)
- Editable design files (AI or PSD)

Templates for the tablecloth and tent attached
Brand guidelines and logos here: https://files.quorbit.net/share/folders/7xKp2Lq9Vn4Rt8Ws1Yb3Hd6JmTq5Fe?usp=share_link

```html
<!DOCTYPE html>
<html lang="en">
<head>
<meta charset="utf-8">
<title>MARLO Event Kit – Booth, Walls, Canopy and Table Cover</title>
<link href="https://fonts.googleapis.com/css2?family=Urbanist:wght@500;700;800;900&display=swap" rel="stylesheet">
<style>
  :root {
    --page: #eeeeee;
    --ink: #1b1b1b;
    --panel: #1a1a1a;
    --teal: #2fd9c4;
    --lime: #d8ee7c;
    --white: #ffffff;
    --bleed: #ef5a2a;
    --label: #222222;
  }
  html, body { margin: 0; padding: 0; overflow: hidden; background: var(--page); }
  .board { display: block; width: 1200px; height: 724px; background: var(--page); }
  .board text { font-family: "Urbanist", sans-serif; }
  .section-label { font-weight: 800; font-size: 11px; fill: var(--label); letter-spacing: -0.2px; }
  .panel { fill: var(--panel); }
  .brand-name { font-weight: 800; fill: var(--teal); letter-spacing: 0.5px; }
  .brand-name--white { fill: var(--white); }
  .brand-mark { fill: var(--teal); }
  .brand-mark--white { fill: var(--white); }
  .tagline { font-weight: 600; font-size: 5.4px; fill: var(--teal); }
  .valance-text { font-weight: 900; font-size: 17px; fill: url(#brandGradient); letter-spacing: -0.6px; }
  .headline-tag { font-weight: 900; font-size: 20px; fill: var(--ink); letter-spacing: -1px; }
  .headline { font-weight: 900; font-size: 28px; fill: var(--white); letter-spacing: -1.4px; }
  .headline-accent { fill: var(--teal); }
  .bleed-text { font-weight: 600; font-size: 5.5px; fill: var(--white); }
  .stat-big { font-weight: 900; fill: var(--teal); }
  .stat-small { font-weight: 600; fill: var(--white); }
  .stat-white { font-weight: 900; fill: var(--white); }
  .stars { font-weight: 700; fill: var(--lime); }
  .swoosh { fill: none; stroke: url(#brandGradient); stroke-linejoin: round; stroke-linecap: round; }
</style>
</head>
<body>
<svg class="board" width="1200" height="724" viewBox="0 0 1200 724" xmlns="http://www.w3.org/2000/svg">
  <defs>
    <linearGradient id="brandGradient" x1="0" y1="0" x2="1" y2="1">
      <stop offset="0" stop-color="#2fd9c4"/>
      <stop offset="1" stop-color="#d8ee7c"/>
    </linearGradient>
    <linearGradient id="houseTone" x1="0" y1="0" x2="1" y2="1">
      <stop offset="0" stop-color="#5b6470"/>
      <stop offset="0.5" stop-color="#e8e8e6"/>
      <stop offset="1" stop-color="#8a8f8a"/>
    </linearGradient>
    <linearGradient id="panelTone" x1="0" y1="0" x2="1" y2="1">
      <stop offset="0" stop-color="#6a78e0"/>
      <stop offset="1" stop-color="#2c3aa8"/>
    </linearGradient>
    <clipPath id="clipBackdrop"><rect x="0" y="0" width="317" height="226"/></clipPath>
    <clipPath id="clipWall"><rect x="0" y="0" width="378" height="145"/></clipPath>
  </defs>

  <!-- Booth backdrop -->
  <text class="section-label" x="183" y="49" text-anchor="middle">Booth Backgrop</text>
  <g class="backdrop" transform="translate(40 63)">
    <rect class="panel" width="317" height="226"/>
    <g clip-path="url(#clipBackdrop)">
      <path class="swoosh" stroke-width="11" d="M-4 50 L44 150 L2 178 C-6 184 -4 205 8 226"/>
      <path class="swoosh" stroke-width="11" d="M298 -4 C310 20 318 30 300 60 C290 80 290 90 310 95 L268 80 L305 160 L322 226"/>
      <path class="swoosh" stroke-width="6" d="M0 -2 L30 -2 L0 12 Z"/>
    </g>
    <g class="logo-grid">
      <g transform="translate(77 31)"><rect class="brand-mark" x="-28" y="-8" width="8" height="8"/><text class="brand-name" x="-17" y="0" font-size="12">MARLO</text><text class="tagline" x="-28" y="8">Get Solar Powered</text></g>
      <g transform="translate(155 31)"><rect class="brand-mark" x="-28" y="-8" width="8" height="8"/><text class="brand-name" x="-17" y="0" font-size="12">MARLO</text><text class="tagline" x="-28" y="8">Get Solar Powered</text></g>
      <g transform="translate(234 31)"><rect class="brand-mark" x="-28" y="-8" width="8" height="8"/><text class="brand-name" x="-17" y="0" font-size="12">MARLO</text><text class="tagline" x="-28" y="8">Get Solar Powered</text></g>
      <g transform="translate(104 71)"><rect class="brand-mark" x="-28" y="-8" width="8" height="8"/><text class="brand-name" x="-17" y="0" font-size="12">MARLO</text><text class="tagline" x="-28" y="8">Get Solar Powered</text></g>
      <g transform="translate(183 71)"><rect class="brand-mark" x="-28" y="-8" width="8" height="8"/><text class="brand-name" x="-17" y="0" font-size="12">MARLO</text><text class="tagline" x="-28" y="8">Get Solar Powered</text></g>
      <g transform="translate(77 111)"><rect class="brand-mark" x="-28" y="-8" width="8" height="8"/><text class="brand-name" x="-17" y="0" font-size="12">MARLO</text><text class="tagline" x="-28" y="8">Get Solar Powered</text></g>
      <g transform="translate(155 111)"><rect class="brand-mark" x="-28" y="-8" width="8" height="8"/><text class="brand-name" x="-17" y="0" font-size="12">MARLO</text><text class="tagline" x="-28" y="8">Get Solar Powered</text></g>
      <g transform="translate(234 111)"><rect class="brand-mark" x="-28" y="-8" width="8" height="8"/><text class="brand-name" x="-17" y="0" font-size="12">MARLO</text><text class="tagline" x="-28" y="8">Get Solar Powered</text></g>
      <g transform="translate(104 150)"><rect class="brand-mark" x="-28" y="-8" width="8" height="8"/><text class="brand-name" x="-17" y="0" font-size="12">MARLO</text><text class="tagline" x="-28" y="8">Get Solar Powered</text></g>
      <g transform="translate(183 150)"><rect class="brand-mark" x="-28" y="-8" width="8" height="8"/><text class="brand-name" x="-17" y="0" font-size="12">MARLO</text><text class="tagline" x="-28" y="8">Get Solar Powered</text></g>
      <g transform="translate(77 190)"><rect class="brand-mark" x="-28" y="-8" width="8" height="8"/><text class="brand-name" x="-17" y="0" font-size="12">MARLO</text><text class="tagline" x="-28" y="8">Get Solar Powered</text></g>
      <g transform="translate(155 190)"><rect class="brand-mark" x="-28" y="-8" width="8" height="8"/><text class="brand-name" x="-17" y="0" font-size="12">MARLO</text><text class="tagline" x="-28" y="8">Get Solar Powered</text></g>
      <g transform="translate(234 190)"><rect class="brand-mark" x="-28" y="-8" width="8" height="8"/><text class="brand-name" x="-17" y="0" font-size="12">MARLO</text><text class="tagline" x="-28" y="8">Get Solar Powered</text></g>
    </g>
  </g>

  <!-- Booth valance front -->
  <g class="valance" transform="translate(40 319)">
    <rect class="panel" width="317" height="28"/>
    <polygon points="0,0 22,0 0,7" fill="url(#brandGradient)"/>
    <polygon points="262,0 300,0 270,10" fill="url(#brandGradient)"/>
    <polygon points="60,28 92,28 86,22" fill="url(#brandGradient)"/>
    <polygon points="300,28 317,28 317,20" fill="url(#brandGradient)"/>
    <text class="valance-text" x="158" y="21" text-anchor="middle">Get Solar Powered</text>
  </g>
  <text class="section-label" x="183" y="373" text-anchor="middle">Booth Valance Front</text>

  <!-- Outer side wall -->
  <text class="section-label" x="581" y="50" text-anchor="middle">Outer Side Walls</text>
  <g class="side-wall side-wall--outer" transform="translate(392 63)">
    <rect class="panel" width="378" height="145"/>
    <g clip-path="url(#clipWall)">
      <path class="swoosh" stroke-width="7" d="M378 5 C330 0 300 20 220 40 C218 70 260 80 240 100 C215 130 220 140 245 150"/>
    </g>
    <rect role="img" aria-label="Photo of a modern white house with rooftop solar panels" x="210" y="28" width="168" height="104" rx="4" fill="url(#houseTone)"/>
    <g transform="rotate(-3 100 52)">
      <rect x="15" y="34" width="168" height="36" fill="var(--teal)"/>
      <text class="headline-tag" x="25" y="62">See How Much</text>
    </g>
    <text class="headline" x="30" y="94">You Can Save</text>
    <text class="headline" x="30" y="123">with <tspan class="headline-accent">Solar!</tspan></text>
  </g>

  <!-- Inner side wall -->
  <g class="side-wall side-wall--inner" transform="translate(392 233)">
    <rect class="panel" width="378" height="145"/>
    <g clip-path="url(#clipWall)">
      <path class="swoosh" stroke-width="7" d="M100 -4 C150 10 150 40 135 60 C120 85 150 100 150 125 C150 140 140 145 130 150"/>
    </g>
    <rect role="img" aria-label="Illustration of two blue solar panels" x="37" y="18" width="107" height="110" rx="3" fill="url(#panelTone)"/>
    <g transform="rotate(-3 237 50)">
      <rect x="153" y="33" width="168" height="36" fill="var(--teal)"/>
      <text class="headline-tag" x="163" y="61">See How Much</text>
    </g>
    <text class="headline" x="168" y="90">You Can Save</text>
    <text class="headline" x="168" y="119">with <tspan class="headline-accent">Solar!</tspan></text>
  </g>
  <text class="section-label" x="580" y="403" text-anchor="middle">Inner Side Walls</text>

  <!-- Booth canopy front -->
  <g class="canopy-front">
    <polygon class="panel" points="957,39 999,39 1152,239 795,239"/>
    <rect class="brand-mark--white" x="904" y="158" width="22" height="22"/>
    <text class="brand-name brand-name--white" x="934" y="188" font-size="36">MARLO</text>
    <text class="section-label" x="1047" y="75">Booth</text>
    <text class="section-label" x="1047" y="87">Canopy Front</text>
    <polyline points="1090,95 1090,121 1061,121" fill="none" stroke="#555" stroke-width="0.6"/>
  </g>

  <!-- Stretch table cover -->
  <g class="stretch-table">
    <rect x="890" y="279" width="155" height="13" fill="var(--bleed)"/>
    <text class="bleed-text" x="967" y="288" text-anchor="middle">3" BLEED</text>
    <rect x="890" y="610" width="155" height="12" fill="var(--bleed)"/>
    <text class="bleed-text" x="967" y="618" text-anchor="middle">3" BLEED</text>
    <rect x="757" y="410" width="13" height="82" fill="var(--bleed)"/>
    <rect x="1165" y="410" width="13" height="82" fill="var(--bleed)"/>
    <polygon class="panel" points="893,296 1042,296 1058,400 1163,408 1163,493 1058,502 1045,606 893,606 878,502 773,493 773,408 878,400"/>
    <polygon points="893,296 945,296 890,322" fill="url(#brandGradient)"/>
    <polygon points="978,395 1030,380 1034,395" fill="url(#brandGradient)"/>
    <polygon points="893,506 950,506 897,520" fill="url(#brandGradient)"/>
    <polygon points="990,603 1040,578 1044,603" fill="url(#brandGradient)"/>
    <g transform="rotate(180 967 346)">
      <rect class="brand-mark" x="931" y="338" width="12" height="12"/>
      <text class="brand-name" x="948" y="353" font-size="20">MARLO</text>
    </g>
    <rect class="brand-mark--white" x="922" y="439" width="18" height="18"/>
    <text class="brand-name brand-name--white" x="946" y="462" font-size="28">MARLO</text>
    <rect class="brand-mark" x="935" y="546" width="12" height="12"/>
    <text class="brand-name" x="952" y="563" font-size="20">MARLO</text>
    <g transform="translate(842 450) rotate(90)">
      <text class="stat-big" x="-28" y="0" font-size="22">500+</text>
      <text class="stat-small" x="-28" y="10" font-size="4.5">Reviews across Canada</text>
      <text class="stat-white" x="-28" y="20" font-size="9">Ratewell</text>
      <text class="stars" x="-28" y="28" font-size="5">★★★★★</text>
    </g>
    <g transform="translate(1103 450) rotate(-90)">
      <text class="stat-white" x="-30" y="-8" font-size="14">03263</text>
      <text class="stat-big" x="-30" y="7" font-size="16">Homes</text>
      <text class="stat-small" x="-30" y="14" font-size="4.5">with Solar by</text>
      <text class="brand-name" x="-30" y="22" font-size="7">MARLO</text>
    </g>
    <text class="section-label" x="960" y="660" text-anchor="middle">Stretch Table</text>
  </g>
</svg>
</body>
</html>
```